Elegant and modern body scrub for organic junkies

I need a package design for my new company based out of Austin, Texas. We are focused on cruelty free and all natural and organic products. Our deign needs to be able to have the information we require on it, while still appearing very clean and captivating. Our initial product is a clear skin body scrub, intended for people with problematic skin. Our target market is women and we want to show elegance, without appearing "high end."
Updates

Reason: I want to allot more time for certain designers to submit edits. Last minute proposals have been appealing

Target Market(s)

Women. Organic and holistic minded. Natural beauty lovers.

Industry/Entity Type

Skin Care Product

Font styles to use
Script
Other font styles liked:
• AmericanTypewriter, Beautifulflaws, courier, caviarDreams-bold

Colors
000000
ffc214
ffffff
fece3e
fbee3e

Requirements
Must have
• Must be designed in Adobe Illustrator.
• The photo titled “structure for oz and grams” -That needs to be included at the bottom of 1B. I like the horizontal and vertical bar that separate the two. I want that.
• Color Inspiration - The photo titled “vorna color inspiration” and “color combo inspiration” are the colors I want. BLACK, GOLD, WHITE. I want the label background black and the writing in white with some gold somewhere on it. My logo is going to be a golden elephant.
• The photos titled “I like how clean this looks” and “I also like how clean this looks” - I want 1B to look super clean. I don’t want a lot of information in this box. I want simple and clean. This is where the logo and brand name will go.
• Logo - A golden elephant. I want it to be gold and geometric. There can be dimension like this elephant example on the left of the 1B description. I want the trunk to be facing to the left and the trunk needs to be raised overhead and touching the animal's forehead.
• The photo titled “sideways writing and silver rim” - I want 1C to be written sideways like this. My text will be much more extensive so the font won’t be able to be so big.
Nice to have
• The photo titled “sideways writing and silver rim” - I want 1C to be written sideways like this. My text will be much more extensive so the font won’t be able to be so big. I also REALLY like how this label is rimmed in silver, but I would want gold. This is not mandatory, but I really like this.
• The photo titled “melted honey” - This is another option I really like. The gold that looks like honey dripping on the label is really cool. Not mandatory, but I really liked that. I also like the craft background on this.
• Color Inspiration - The photo titled “color inspiration” and “another color inspiration” is an option I would also like to see. Rather than black, I’d like to see what it would ALSO look like with a navy background. NAVY, GOLD, WHITE, maybe black somewhere.
Should not have
• Colorful patterns or excessive info in section 1B.

```html
<!DOCTYPE html>
<html lang="en">
<head>
<meta charset="utf-8">
<title>Clear Skin Body Polish – Jar Label</title>
<link rel="stylesheet" href="https://fonts.googleapis.com/css2?family=Dancing+Script:wght@500&family=Courier+Prime&family=Montserrat:wght@300;400&display=swap">
<style>
  :root {
    --navy: #1a2650;
    --navy-deep: #141e42;
    --gold: #c29a5b;
    --gold-light: #d9b77a;
    --white: #ffffff;
    --page: #ffffff;
  }
  * { box-sizing: border-box; margin: 0; padding: 0; }
  html, body { width: 1200px; height: 770px; overflow: hidden; background: var(--page); }

  .label {
    position: absolute;
    left: 20px; top: 290px;
    width: 1160px; height: 190px;
    background: var(--navy);
    color: var(--white);
    font-family: "Montserrat", sans-serif;
    font-weight: 300;
  }
  .label__rim { position: absolute; left: 0; top: 0; width: 100%; height: 12px; }

  /* Directions panel */
  .directions { position: absolute; left: 8px; top: 16px; width: 350px; font-size: 7.6px; line-height: 1.32; }
  .directions__tagline { font-family: "Dancing Script", cursive; font-size: 11.5px; margin-bottom: 4px; }
  .directions p { margin-bottom: 1px; }
  .claims {
    display: flex; margin-top: 7px; width: 336px;
    border: 1px solid var(--gold);
    font-size: 8.3px; letter-spacing: 0.8px; line-height: 1.25; text-transform: uppercase;
  }
  .claims__item { padding: 5px 7px; display: flex; align-items: center; }
  .claims__item + .claims__item { border-left: 1px solid var(--gold); }
  .claims__item--organic { width: 70px; }
  .claims__item--cruelty { width: 102px; }
  .claims__item--free { flex: 1; }
  .recycle { display: flex; align-items: center; gap: 8px; margin-top: 8px; font-size: 7.6px; }

  /* Brand panel */
  .brand-name {
    position: absolute; left: 364px; top: 14px; height: 166px; width: 22px;
    writing-mode: vertical-rl; transform: rotate(180deg);
    font-family: "Courier Prime", monospace; font-size: 16px; letter-spacing: 2.5px;
    text-align: center;
  }
  .brand-mark { position: absolute; left: 410px; top: 26px; width: 118px; height: 124px; }
  .product { position: absolute; left: 550px; top: 106px; width: 122px; font-family: "Courier Prime", monospace; text-align: right; }
  .product__name { font-size: 13.5px; letter-spacing: 1.2px; line-height: 1.95; }
  .product__size { display: flex; justify-content: flex-end; margin-top: 4px; font-size: 13px; letter-spacing: 1px; border-top: 1px solid var(--gold); }
  .product__size span { padding: 3px 10px 0; }
  .product__size span + span { border-left: 1px solid var(--gold); padding-right: 2px; }

  /* Story panel */
  .tagline-side {
    position: absolute; left: 684px; top: 22px; height: 160px; width: 44px;
    writing-mode: vertical-rl; transform: rotate(180deg);
    font-family: "Dancing Script", cursive; font-size: 13px; line-height: 1.35;
  }
  .drip { position: absolute; left: 712px; top: 0; width: 12px; height: 80px; }
  .story {
    position: absolute; left: 740px; top: 30px; width: 328px; height: 150px;
    column-count: 2; column-gap: 12px;
    font-size: 7.1px; line-height: 1.27; text-align: justify;
  }
  .story p { margin-bottom: 2px; }
  .code-space { position: absolute; left: 1079px; top: 12px; width: 46px; height: 166px; background: var(--white); }
</style>
</head>
<body>
  <section class="label" aria-label="Clear Skin Body Polish jar label">
    <svg class="label__rim" viewBox="0 0 1160 12" preserveAspectRatio="none" aria-hidden="true">
      <rect x="0" y="0" width="1160" height="3.5" fill="var(--gold)"/>
      <path d="M0 6 H1160" stroke="var(--gold-light)" stroke-width="0.8" fill="none"/>
    </svg>

    <div class="directions">
      <h2 class="directions__tagline">Handmade in small batches with Love</h2>
      <p>Directions: Shake well before use. Gently massage scrub in circular motions over wet skin (not face). Pay special attention to rough or dry patches. After use, a residual layer of oil will remain on skin. Rinse thoroughly and pat dry with towel. Skin will feel elegantly soft and nourished. Avoid use on freshly shaven or broken skin.</p>
      <p>Caution: Oils in product may leave shower or tub surfaces slippery. Not intended for facial use. Essential oils or use on freshly shaven skin may cause skin irritation. External use only.</p>
      <div class="claims">
        <div class="claims__item claims__item--organic">All<br>Organic</div>
        <div class="claims__item claims__item--cruelty">Never<br>Tested<br>on Animals</div>
        <div class="claims__item claims__item--free">Free of: Fragrance,<br>Parabens, Synthetic<br>Ingredients, Chemicals</div>
      </div>
      <div class="recycle">
        <span>Please recycle. I want to come back as a solar panel.</span>
        <svg width="12" height="11" viewBox="0 0 12 11" aria-hidden="true">
          <path d="M6 1 L9 6 M9 6 L7.6 5.4 M9 6 L9.3 4.5 M10 8 H3 M3 8 L4.2 7 M3 8 L4.2 9 M2 6.5 L5 1.5 M5 1.5 L3.5 2 M5 1.5 L5.3 3" stroke="#e8e8e8" stroke-width="1.1" fill="none" stroke-linecap="round"/>
        </svg>
      </div>
    </div>

    <h1 class="brand-name">BRAND NAME</h1>
    <svg class="brand-mark" viewBox="0 0 118 124" role="img" aria-label="Golden elephant logo with raised trunk facing left">
      <defs>
        <radialGradient id="markGlow" cx="50%" cy="50%" r="55%">
          <stop offset="0%" stop-color="var(--gold-light)"/>
          <stop offset="100%" stop-color="var(--gold)"/>
        </radialGradient>
      </defs>
      <rect x="0" y="0" width="118" height="124" rx="6" fill="url(#markGlow)"/>
    </svg>

    <div class="product">
      <div class="product__name">Clear Skin<br>Body polish</div>
      <div class="product__size"><span>12oz</span><span>340g</span></div>
    </div>

    <svg class="drip" viewBox="0 0 12 80" aria-hidden="true">
      <path d="M4 0 H8 V68 C8 71 10 73 10 75.5 A4 4 0 0 1 2 75.5 C2 73 4 71 4 68 Z" fill="var(--gold)"/>
    </svg>
    <p class="tagline-side">Made with naturally derived ingredients only</p>

    <div class="story">
      <p>The combination of ingredients in this loving scrub were chosen with problematic body skin in mind. The high concentration of magnesium in Dead Sea Salt is instrumental in improving skin hydration and reducing inflammation.</p>
      <p>Pink salt is readily absorbed into the skin, cleansing and purifying the pores from the inside out. It can improve the texture, tone, and appearance of the skin.</p>
      <p>This loving essential oil concoction helps fight acne by removing toxins and cleaning sebaceous glands. Some EOs contain strong antibacterial, antifungal, and anti inflammatory properties. Certain EOs inhibit the bacteria that cause skin infections as well as target acne scarring and pigmentation from previous breakouts.</p>
      <p>Each of these ingredients plays an elemental role in anti aging, as well as fighting problematic skin. Use this skin polish regularly to receive prime results.</p>
      <p>Ingredients: Dead Sea Salt, Pink Himalayan Salt, Coconut oil, Argan Oil, Jojoba Oil, Almond Oil, Lavender EO, Tea Tree EO, Geranium EO, Chamomile EO, Frankincense EO, Bergamot EO, Rosemary EO.</p>
    </div>

    <div class="code-space"></div>
  </section>
</body>
</html>
```